Kindle the Quiet Summit is a guide to help individuals overcome obstacles that they face in their life. This book provides thought provoking concepts that allow individuals to work through challenges if their life. The cover needs to be powerful! It needs to speak to the reader of breaking free of problems and overcoming challenges.

Kindle The Quiet Summit
A Handbook for climbing past hardships and growing into the self you were destined to become.
By
Dr. Marcus J. Belcroft

```html
<!DOCTYPE html>
<html lang="en">
<head>
<meta charset="utf-8">
<title>Kindle The Quiet Summit — Book Cover</title>
<link rel="stylesheet" href="https://fonts.googleapis.com/css2?family=Cinzel:wght@400;500;600&family=Libre+Baskerville:ital@1&display=swap">
<style>
  :root {
    --page-bg: #ffffff;
    --wall-light: #f2f1ef;
    --wall-mid: #bdb9b5;
    --shadow-dark: #3e3835;
    --ledge: #3a302b;
    --ledge-top: #4a3f39;
    --title-dark: #2f2926;
    --title-gold: #d2a96c;
    --outline-fill: #f4f2ef;
    --subtitle: #ffffff;
    --author: #ece8e3;
  }
  * { margin: 0; padding: 0; box-sizing: border-box; }
  html, body {
    width: 1200px; height: 900px; overflow: hidden;
    background: var(--page-bg);
  }
  .canvas { position: relative; width: 1200px; height: 900px; }
  .cover {
    position: absolute; left: 281px; top: 0;
    width: 638px; height: 900px; overflow: hidden;
    background: var(--wall-light);
  }
  .cover-art { position: absolute; left: 0; top: 0; width: 638px; height: 735px; display: block; }
  .ledge {
    position: absolute; left: 0; top: 735px; width: 638px; height: 165px;
    background: linear-gradient(to bottom, var(--ledge-top), var(--ledge) 30%);
  }
  .title {
    position: absolute; left: 0; top: 14px; width: 638px;
    text-align: center; font-family: "Cinzel", serif; color: var(--title-dark);
    line-height: 1;
  }
  .title-lead { display: block; font-size: 46px; letter-spacing: 2px; font-weight: 500; }
  .title-lead .cap { font-size: 60px; }
  .title-key {
    display: block; font-size: 132px; color: var(--title-gold);
    letter-spacing: 10px; font-weight: 500; margin-top: 4px;
  }
  .title-tail { display: block; font-size: 54px; letter-spacing: 4px; margin-top: 2px; }
  .title-tail .cap { font-size: 72px; }
  .title-tail .outlined {
    color: var(--outline-fill);
    -webkit-text-stroke: 1.3px var(--title-dark);
  }
  .subtitle {
    position: absolute; left: 250px; top: 282px; width: 330px;
    text-align: center; font-family: "Libre Baskerville", serif; font-style: italic;
    font-size: 24px; line-height: 31px; letter-spacing: 2px; color: var(--subtitle);
  }
  .author {
    position: absolute; left: 0; top: 810px; width: 638px; text-align: center;
    font-family: "Cinzel", serif; font-size: 29px; letter-spacing: 3px; color: var(--author);
  }
  .author .cap { font-size: 36px; }
</style>
</head>
<body>
<main class="canvas">
  <section class="cover">
    <svg class="cover-art" viewBox="0 0 638 735" role="img" aria-label="Orange tabby cat seated on a ledge, casting a large lion-shaped shadow on a pale wall">
      <defs>
        <radialGradient id="wallGlow" cx="0.12" cy="0.45" r="0.8">
          <stop offset="0" stop-color="#f4f3f1"/>
          <stop offset="0.6" stop-color="#dcd9d6"/>
          <stop offset="1" stop-color="#aaa6a2"/>
        </radialGradient>
        <radialGradient id="shadowCast" cx="0.62" cy="0.5" r="0.5">
          <stop offset="0" stop-color="#3e3835"/>
          <stop offset="0.7" stop-color="#4a4441" stop-opacity="0.9"/>
          <stop offset="1" stop-color="#4a4441" stop-opacity="0"/>
        </radialGradient>
        <radialGradient id="catTone" cx="0.5" cy="0.5" r="0.5">
          <stop offset="0" stop-color="#e0a95e"/>
          <stop offset="1" stop-color="#e0a95e" stop-opacity="0"/>
        </radialGradient>
      </defs>
      <rect width="638" height="735" fill="url(#wallGlow)"/>
      <ellipse cx="400" cy="430" rx="270" ry="340" fill="url(#shadowCast)"/>
      <ellipse cx="180" cy="600" rx="130" ry="150" fill="url(#catTone)"/>
    </svg>
    <div class="ledge"></div>

    <h1 class="title">
      <span class="title-lead"><span class="cap">K</span>INDLE <span class="cap">T</span>HE</span>
      <span class="title-key">QUIET</span>
      <span class="title-tail"><span class="cap">S</span>U<span class="outlined">MMIT</span></span>
    </h1>

    <p class="subtitle">A Handbook for climbing past hardships and growing into the self you were destined to become.</p>

    <p class="author"><span class="cap">D</span>R. <span class="cap">M</span>ARCUS <span class="cap">J</span>. <span class="cap">B</span>ELCROFT</p>
  </section>
</main>
</body>
</html>
```